Measuring Card for Eyelash Extensions

I want this made for my brand and in a format that I can get printed on standard size business cards (3.5 x 2 inches). The measurement must be accurate to the end of the business card because this will be put up to the eye to measure the lash length.
This is being sent to lash extension artists so they can measure the natural lash before they begin applying eyelash extensions. I want it to look like the card I attached and it must be an accurate measurement.

Target Market(s)

Lash Extension Artists

Font styles to use
Sans Serif

Colors
ffffff

Requirements
Must have
• Must be accurate measurement on a 3.5 x 2 inch business card.
Nice to have
• To look very similar to the card in the photo I attached.

```html
<!DOCTYPE html>
<html lang="en">
<head>
<meta charset="utf-8">
<title>Lash Length Measuring Card</title>
<link href="https://fonts.googleapis.com/css2?family=Open+Sans:wght@400;600;700&display=swap" rel="stylesheet">
<style>
  :root {
    --page: #ebeceb;
    --card: #ffffff;
    --card-edge: #dcdcdc;
    --plum: #2a0b5f;
    --ink: #2d1466;
    --sand: #c8a48c;
    --photo-tone: #b9a89a;
  }
  * { margin: 0; padding: 0; box-sizing: border-box; }
  html, body { width: 1027px; height: 1200px; overflow: hidden; }
  body { background: var(--page); font-family: "Open Sans", Arial, sans-serif; position: relative; }

  .card {
    position: absolute; left: 292px; top: 206px; width: 450px; height: 788px;
    background: var(--card); border: 1px solid var(--card-edge);
  }
  .title-tab {
    position: absolute; left: 0; top: 0; width: 303px; height: 47px;
    background: var(--plum); color: #fff; font-weight: 700; font-size: 21px;
    line-height: 47px; padding-left: 22px; letter-spacing: 0.2px;
  }
  .brand {
    position: absolute; left: 22px; top: 52px; right: 26px;
  }
  .brand-name {
    font-size: 40px; font-weight: 400; color: var(--ink); letter-spacing: 4px; line-height: 56px;
  }
  .brand-tagline {
    text-align: right; font-size: 11px; color: var(--ink); letter-spacing: 0.5px; margin-top: 16px;
  }
  .section-band {
    position: absolute; left: 0; top: 154px; width: 100%; height: 43px;
    background: var(--sand); color: #fff; font-weight: 700; font-size: 20px;
    text-align: center; line-height: 43px;
  }
  .guidance {
    position: absolute; left: 44px; top: 197px; width: 363px;
    font-size: 18.5px; line-height: 28px; color: var(--ink); text-align: justify; letter-spacing: 0.3px;
  }
  .divider {
    position: absolute; left: 0; width: 100%; border-top: 2px dotted var(--sand);
  }
  .divider.upper { top: 337px; }
  .divider.lower { top: 594px; }
  .example-photo {
    position: absolute; left: 72px; top: 345px; width: 174px; height: 152px;
    border: 10px solid var(--plum);
    background: linear-gradient(180deg, #d8d5d2 0%, #b7aca4 70%, #c49a8a 100%);
  }
  .example-text {
    position: absolute; left: 70px; top: 500px; color: var(--ink);
    font-weight: 700; font-size: 21px; line-height: 30px;
  }
  .ruler { position: absolute; left: 198px; top: 600px; }
</style>
</head>
<body>
  <main class="card">
    <div class="title-tab">MEASURE LASH LENGTH</div>

    <div class="brand">
      <div class="brand-name">LUMA LASH</div>
      <div class="brand-tagline">CUSTOM LASH SUPPLY</div>
    </div>

    <div class="section-band">SAFE LENGTHS</div>

    <p class="guidance">It is not recommended to apply lash extensions that are longer than +3mm from the natural lash length. For inner corners, try not to apply any longer than +1mm.</p>

    <div class="divider upper"></div>

    <div class="example-photo" role="img" aria-label="Close-up photo of natural lashes held against a millimetre scale reading up to 10mm"></div>

    <div class="example-text">
      Example:<br>
      Natural Lash: 9mm<br>
      MAXIMUM Extension: 12mm
    </div>

    <div class="divider lower"></div>

    <svg class="ruler" width="120" height="188" viewBox="0 0 120 188" aria-label="Millimetre ruler from card edge">
      <g stroke="#2a0b5f" stroke-width="1">
        <line x1="4" y1="182.6" x2="14" y2="182.6"/><line x1="4" y1="178.2" x2="20" y2="178.2"/>
        <line x1="4" y1="173.8" x2="14" y2="173.8"/><line x1="4" y1="169.4" x2="20" y2="169.4"/>
        <line x1="4" y1="165" x2="14" y2="165"/><line x1="4" y1="160.6" x2="20" y2="160.6"/>
        <line x1="4" y1="156.2" x2="14" y2="156.2"/><line x1="4" y1="151.8" x2="20" y2="151.8"/>
        <line x1="4" y1="147.4" x2="14" y2="147.4"/><line x1="4" y1="143" x2="46" y2="143"/>
        <line x1="4" y1="138.6" x2="14" y2="138.6"/><line x1="4" y1="134.2" x2="20" y2="134.2"/>
        <line x1="4" y1="129.8" x2="14" y2="129.8"/><line x1="4" y1="125.4" x2="20" y2="125.4"/>
        <line x1="4" y1="121" x2="14" y2="121"/><line x1="4" y1="116.6" x2="20" y2="116.6"/>
        <line x1="4" y1="112.2" x2="14" y2="112.2"/><line x1="4" y1="107.8" x2="20" y2="107.8"/>
        <line x1="4" y1="103.4" x2="14" y2="103.4"/><line x1="4" y1="99" x2="46" y2="99"/>
        <line x1="4" y1="94.6" x2="14" y2="94.6"/><line x1="4" y1="90.2" x2="20" y2="90.2"/>
        <line x1="4" y1="85.8" x2="14" y2="85.8"/><line x1="4" y1="81.4" x2="20" y2="81.4"/>
        <line x1="4" y1="77" x2="14" y2="77"/><line x1="4" y1="72.6" x2="20" y2="72.6"/>
        <line x1="4" y1="68.2" x2="14" y2="68.2"/><line x1="4" y1="63.8" x2="20" y2="63.8"/>
        <line x1="4" y1="59.4" x2="14" y2="59.4"/><line x1="4" y1="55" x2="46" y2="55"/>
        <line x1="4" y1="50.6" x2="14" y2="50.6"/><line x1="4" y1="46.2" x2="20" y2="46.2"/>
        <line x1="4" y1="41.8" x2="14" y2="41.8"/><line x1="4" y1="37.4" x2="20" y2="37.4"/>
        <line x1="4" y1="33" x2="14" y2="33"/><line x1="4" y1="28.6" x2="20" y2="28.6"/>
        <line x1="4" y1="24.2" x2="14" y2="24.2"/><line x1="4" y1="19.8" x2="20" y2="19.8"/>
        <line x1="4" y1="15.4" x2="14" y2="15.4"/><line x1="4" y1="11" x2="46" y2="11"/>
      </g>
      <g fill="#c8a48c" font-family="Open Sans, Arial, sans-serif" font-size="6.5">
        <text x="24" y="180.6">01</text><text x="24" y="171.8">02</text><text x="24" y="163">03</text><text x="24" y="154.2">04</text>
        <text x="24" y="136.6">06</text><text x="24" y="127.8">07</text><text x="24" y="119">08</text><text x="24" y="110.2">09</text>
        <text x="24" y="92.6">11</text><text x="24" y="83.8">12</text><text x="24" y="75">13</text><text x="24" y="66.2">14</text>
        <text x="24" y="48.6">16</text><text x="24" y="39.8">17</text><text x="24" y="31">18</text><text x="24" y="22.2">19</text>
      </g>
      <g fill="#c8a48c" font-family="Open Sans, Arial, sans-serif" font-size="15" font-weight="700">
        <text x="47" y="148">05 mm</text>
        <text x="47" y="104">10 mm</text>
        <text x="47" y="60">15 mm</text>
        <text x="47" y="16">20 mm</text>
      </g>
    </svg>
  </main>
</body>
</html>
```